Coffee House With Cycling Theme Wants Business Cards

We want to create a business card for a coffee house that has a cycling theme. We expect to use the current logo on one side of the business card and we have been considering adding the words 'COFFEE HOUSE' underneath (see example). For the other side of the business card we want an interesting design with tag-line, address and social media links (the normal business card stuff). See examples provided but we are not fixed on having it exactly as shown, we are very open to great creative ideas. Please note our logo has the initials ‘RV' in orange embedded in the design and this must be retained. However, you can play with the words COFFEE HOUSE as well as use the orange color on the backside of the business card, as you see fit. For an image on the backside of the business card it can be a photo, hand-drawn or whatever but it must visually combine coffee and cycling in some way. The interior of the Coffee House will be reclaimed wood, rustic and have an urban feel to it with cycling artifacts hanging from the walls/ceiling, etc. Finally, it would be beneficial if the business card design elements can be easily used on flyers and other promotional assets. Good luck, we are looking forward to seeing your creative ideas.

Target Market(s)

Coffee lovers and cycling fans

Contact Information for Business Card

See project description.

Colors

Designer to choose colors to be used in the design.

Requirements
Must have
• Must use the current logo provided and combine a coffee and bike theme.
Nice to have
• Orange is used in current logo and could be used as an accent color on the backside of the business card.

```html
<!DOCTYPE html>
<html lang="en">
<head>
<meta charset="utf-8">
<title>RV Coffee House – Business Cards</title>
<link rel="stylesheet" href="https://fonts.googleapis.com/css2?family=Montserrat:wght@700;800&family=Arimo:wght@400;700&display=swap">
<style>
  :root {
    --backdrop: #a9b4c8;
    --card-white: #e8eaee;
    --orange: #e0652e;
    --brown: #5a2a14;
    --charcoal: #333333;
    --cream: #f5f1ec;
    --foam-light: #e6e1da;
    --foam-dark: #b8ada2;
  }
  * { box-sizing: border-box; margin: 0; padding: 0; }
  html, body {
    width: 1200px; height: 675px; overflow: hidden;
    background: var(--backdrop);
  }
  .sheet {
    position: relative; width: 1200px; height: 675px;
    display: flex; align-items: center; justify-content: center; gap: 40px;
  }
  .card {
    position: relative; width: 540px; height: 309px; overflow: hidden;
    box-shadow: 0 6px 18px rgba(40, 50, 70, 0.25);
  }

  /* Front */
  .card-front {
    background: var(--card-white);
    display: flex; align-items: center; justify-content: center;
  }
  .brand {
    display: flex; align-items: center; gap: 16px;
  }
  .brand-dot {
    width: 54px; height: 54px; border-radius: 50%;
    background: var(--orange);
  }
  .brand-name {
    font-family: "Montserrat", sans-serif; font-weight: 800;
    font-size: 34px; letter-spacing: 1px; color: var(--brown);
  }

  /* Back */
  .card-back { background: var(--orange); }
  .back-art {
    position: absolute; inset: 0; width: 100%; height: 100%;
  }
  .back-info {
    position: absolute; left: 0; top: 0; width: 290px; height: 100%;
    padding: 32px 0 0 34px;
    font-family: "Arimo", sans-serif; color: #ffffff;
  }
  .back-title {
    display: inline-block;
    font-family: "Montserrat", sans-serif; font-weight: 800;
    font-size: 17px; letter-spacing: 1px; color: #ffffff;
  }
  .address {
    margin-top: 10px; font-size: 12.5px; line-height: 1.45;
    letter-spacing: 1.6px; text-align: center; width: 220px;
  }
  .divider {
    margin: 18px 0 0 20px; width: 200px; height: 2px;
    background: var(--brown); border-radius: 2px;
  }
  .website {
    margin: 18px 0 0 40px; font-size: 11px; font-weight: 700; letter-spacing: 1.8px;
  }
  .socials { list-style: none; margin: 14px 0 0 20px; }
  .social {
    display: flex; align-items: center; gap: 12px; margin-bottom: 9px;
    font-size: 10.5px; font-weight: 700; letter-spacing: 1.8px;
  }
  .social-dot {
    width: 26px; height: 26px; border-radius: 50%; background: var(--cream);
  }
</style>
</head>
<body>
<main class="sheet">
  <section class="card card-front" aria-label="Business card front">
    <div class="brand">
      <span class="brand-dot"></span>
      <span class="brand-name">RV COFFEE HOUSE</span>
    </div>
  </section>

  <section class="card card-back" aria-label="Business card back">
    <svg class="back-art" viewBox="0 0 540 309" preserveAspectRatio="none">
      <defs>
        <radialGradient id="foam" cx="0.6" cy="0.4" r="0.7">
          <stop offset="0" stop-color="var(--foam-light)"/>
          <stop offset="0.7" stop-color="var(--foam-dark)"/>
          <stop offset="1" stop-color="#d6dbe0"/>
        </radialGradient>
      </defs>
      <path role="img" aria-label="Photo of a cappuccino with a bicycle drawn in cocoa on the milk foam"
            d="M300 0 Q 270 160 330 309 L540 309 L540 0 Z" fill="url(#foam)"/>
      <path d="M300 0 Q 270 160 330 309" fill="none" stroke="var(--brown)" stroke-width="9"/>
    </svg>
    <div class="back-info">
      <h2 class="back-title">COFFEE HOUSE</h2>
      <p class="address">218 Larkfield Street<br>Millbrook, NY 12545<br>555-014-2290</p>
      <div class="divider"></div>
      <p class="website">RVCOFFEEHOUSE.COM</p>
      <ul class="socials">
        <li class="social"><span class="social-dot"></span>RVCOFFEEHOUSE</li>
        <li class="social"><span class="social-dot"></span>RVCOFFEEHOUSE</li>
        <li class="social"><span class="social-dot"></span>RVCOFFEEHOUSE</li>
      </ul>
    </div>
  </section>
</main>
</body>
</html>
```